Ecommerce Web Design - We currently have a live website running on https://www.brivonta.co.za - this website must be redesigned for an eCommerce website since we are moving to sell our items online. Kindly put a new design utilising the information from the current live website

Link to Pictures & Brochure: https://files.tarvelox.example/share/f/pelumo_drastin_co_za/Xq7LmPz3RtY9vNw2KsHbJd4?e=Q8rT2m

```html
<!DOCTYPE html>
<html lang="en">
<head>
<meta charset="utf-8">
<title>Brivonta – Ladders, Trolleys &amp; Accessories</title>
<link rel="stylesheet" href="https://fonts.googleapis.com/css2?family=Roboto:wght@400;500;700&family=Poppins:wght@400;500;600&display=swap">
<style>
:root{
  --blue:#0b5aaa;
  --blue-dark:#084a8c;
  --hero:#c9d9f3;
  --ink:#222;
  --muted:#777;
  --soft:#f5f5f6;
  --line:#e3e3e3;
  --star:#f2b705;
  --dark:#232323;
  --darker:#1c1c1c;
}
*{box-sizing:border-box;margin:0;padding:0}
html,body{width:1200px;height:3188px;overflow:hidden}
body{font-family:"Poppins",sans-serif;color:var(--ink);background:#fff;font-size:12px}
.wrap{width:884px;margin:0 auto;position:relative}
a{color:inherit;text-decoration:none}

/* top bar */
.topbar{height:25px;border-bottom:1px solid #eee;font-size:8px;color:#555}
.topbar .wrap{display:flex;justify-content:space-between;align-items:center;height:25px}
.topbar .acct{display:flex;gap:6px;align-items:center}
.topbar .acct b{color:var(--blue);font-weight:500}

/* header */
.header{height:81px}
.header .wrap{display:flex;align-items:center;height:81px}
.brand{display:flex;align-items:center;gap:8px;width:160px;flex-shrink:0}
.brand .mark{width:26px;height:26px;background:var(--blue)}
.brand span{font-family:"Roboto",sans-serif;font-weight:700;font-size:20px;color:var(--blue)}
.search{width:347px;flex-shrink:0;height:30px;border:1px solid #ddd;border-radius:16px;display:flex;align-items:center;font-size:8.5px;color:#777;overflow:hidden;white-space:nowrap}
.search .cat{width:96px;padding-left:12px;border-right:1px solid #ddd;height:18px;display:flex;align-items:center;justify-content:space-between;padding-right:10px}
.search .q{flex:1;padding-left:12px}
.search .go{width:32px;height:30px;background:var(--blue);border-radius:16px;display:flex;align-items:center;justify-content:center}
.hinfo{display:flex;align-items:center;gap:7px;font-size:7.5px;white-space:nowrap;flex-shrink:0;line-height:1.3}
.hinfo strong{display:block;color:var(--blue);font-size:11px;font-weight:600}
.hinfo .ico{position:relative;display:flex}
.badge{position:absolute;top:-4px;right:-5px;width:12px;height:12px;border-radius:50%;background:#d32f2f;color:#fff;font-size:7px;display:flex;align-items:center;justify-content:center}

/* nav */
.nav{height:36px;background:var(--blue)}
.nav .wrap{display:flex;align-items:center;height:36px}
.allcat{width:143px;height:32px;background:var(--darker);border-radius:16px;color:#fff;display:flex;align-items:center;gap:8px;padding-left:14px;font-size:10px;font-weight:500}
.nav ul{list-style:none;display:flex;margin-left:32px;gap:0}
.nav li{color:#fff;font-size:9.5px;font-weight:500;margin-right:45px;white-space:nowrap}

/* hero */
.hero{height:344px;background:var(--hero);position:relative}
.hero .text{position:absolute;left:158px;top:85px}
.hero .kicker{font-family:"Roboto",sans-serif;font-size:15px;color:#333}
.hero h1{font-family:"Roboto",sans-serif;font-size:46px;font-weight:400;color:#222;line-height:1.05;margin-top:4px}
.hero h1 b{color:var(--blue);font-weight:700}
.hero p{font-size:14px;color:#222;margin-top:10px;line-height:1.45;width:460px}
.btn{display:inline-flex;align-items:center;gap:8px;background:var(--blue);color:#fff;border-radius:16px;font-size:9px;font-weight:500;height:26px;padding:0 16px}
.hero .btn{margin-top:20px;height:28px;padding:0 18px}
.hero .visual{position:absolute;left:755px;top:62px;width:287px;height:216px;border-radius:10px;background:linear-gradient(160deg,#6a9fd8,#2e6aa8)}
.hero .arrow{position:absolute;top:150px}
.dots{position:absolute;left:576px;top:295px;display:flex;gap:6px;align-items:center}
.dots i{width:10px;height:10px;border-radius:50%;background:#111;display:block}
.dots i.on{width:14px;height:14px;background:none;border:1.5px solid var(--blue)}

/* features */
.features{height:180px}
.features .wrap{display:flex;padding-top:46px}
.feat{flex:1;text-align:center;border-right:1px solid var(--line);height:80px}
.feat:last-child{border-right:0}
.feat h4{font-family:"Roboto",sans-serif;font-size:11px;font-weight:500;margin-top:8px}
.feat p{font-size:9px;color:var(--muted);margin-top:2px}

/* section headings */
.sec-title{text-align:center;font-family:"Roboto",sans-serif;font-weight:700;font-size:25px;text-transform:uppercase}
.sec-title span{color:var(--blue)}
.sec-lede{text-align:center;font-size:9.5px;color:#666;line-height:1.6;width:420px;margin:10px auto 0}

/* categories */
.categories{height:379px;background:var(--soft);padding-top:42px}
.cat-row{display:flex;gap:18px;margin-top:32px;position:relative}
.cat{width:132px;height:162px;border:1px solid #ccc;background:#fff;text-align:center;padding-top:7px}
.cat .pic{width:90px;height:90px;margin:0 auto;border-radius:6px;background:linear-gradient(180deg,#dbe6f5,#a9c2e4)}
.cat .pic.ladder{background:linear-gradient(180deg,#f7e2a8,#e7a93a)}
.cat h5{font-family:"Roboto",sans-serif;font-size:10px;font-weight:500;margin:10px 0 8px}
.slide{position:absolute;width:22px;height:22px;border-radius:50%;background:var(--blue);display:flex;align-items:center;justify-content:center}

/* products */
.products{height:600px;padding-top:55px}
.tabs{display:flex;justify-content:center;gap:26px;margin-top:38px;font-family:"Roboto",sans-serif;font-size:11px;font-weight:500}
.tabs span{padding:0 8px 4px}
.tabs .on{color:var(--blue);border-top:2px solid var(--blue);border-bottom:1px solid var(--blue);padding-top:4px;margin-top:-6px}
.grid{display:flex;gap:17px;position:relative}
.products .grid{margin-top:38px}
.card{width:208px;height:304px;background:var(--soft);border:1px solid #e6e6e6;border-radius:6px;position:relative;padding:0 13px}
.card .pic{height:182px;margin:0 6px;border-bottom:1px solid #ddd;display:flex;justify-content:center;align-items:center}
.card .pic div{width:90px;height:160px;border-radius:6px;background:linear-gradient(180deg,#e98a8a,#c42a2a)}
.off{position:absolute;top:18px;right:15px;width:38px;height:38px;border-radius:50%;background:var(--blue);color:#fff;font-size:8.5px;line-height:1.1;text-align:center;padding-top:9px;border:2px solid #fff;box-shadow:0 0 0 1px var(--blue)}
.card .cn{font-size:8.5px;margin-top:12px}
.card h6{font-family:"Roboto",sans-serif;color:var(--blue);font-size:11px;font-weight:500;margin-top:8px;white-space:nowrap}
.stars{color:var(--star);font-size:10px;letter-spacing:2px;margin-top:10px}
.stars em{color:#d9c27a;font-style:normal}
.card .foot{position:absolute;left:13px;right:11px;bottom:10px;display:flex;justify-content:space-between;align-items:flex-end}
.cartbtn{width:27px;height:27px;border-radius:50%;background:var(--blue);display:flex;align-items:center;justify-content:center}
.price{text-align:right;font-family:"Roboto",sans-serif}
.price s{display:block;color:#999;font-size:11px}
.price b{color:var(--blue);font-size:15px}

/* why */
.why{height:293px;background:var(--blue);color:#fff;padding-top:48px}
.why .sec-lede{color:#fff}
.why-row{display:flex;justify-content:space-between;width:900px;margin:22px auto 0}
.why-item{width:260px;text-align:center}
.why-item .ring{width:58px;height:58px;border-radius:50%;border:1.5px solid #fff;margin:0 auto;display:flex;align-items:center;justify-content:center}
.why-item h4{font-family:"Roboto",sans-serif;font-size:11px;font-weight:700;margin-top:12px}
.why-item p{font-size:9px;margin-top:2px}

/* latest */
.latest{height:530px;padding-top:55px}
.latest .grid{margin-top:38px}

/* brands */
.brands{height:303px;background:var(--soft);padding-top:42px}
.brand-row{display:flex;margin-top:36px;background:#fff;border:1px solid #ddd;height:115px}
.brand-row div{flex:1;border-right:1px solid #ddd;display:flex;align-items:center;justify-content:center;font-family:"Roboto",sans-serif;font-weight:700;font-size:17px;color:#9a9a9a}
.brand-row div:last-child{border-right:0}

/* subscribe */
.subscribe{height:183px;background:var(--dark);color:#fff;text-align:center;padding-top:35px;border-bottom:1px solid #3a3a3a}
.subscribe h3{font-family:"Roboto",sans-serif;font-weight:400;font-size:25px;margin-top:6px}
.subscribe p{font-size:10px;margin-top:10px}
.sub-form{display:flex;width:308px;height:28px;margin:12px auto 0;border-radius:16px;overflow:hidden}
.sub-form span{flex:1;background:#fff;color:#666;font-size:9.5px;text-align:left;padding-left:18px;display:flex;align-items:center}
.sub-form b{width:88px;background:var(--blue);font-size:9px;font-weight:500;display:flex;align-items:center;justify-content:center}

/* footer */
.footer{height:234px;background:var(--dark);color:#fff;text-align:center;position:relative}
.footer .brand{justify-content:center;width:auto;padding-top:30px}
.footer .brand span{color:#fff}
.footer .brand .mark{background:var(--blue)}
.flinks{display:flex;justify-content:center;gap:19px;font-size:9px;margin-top:36px}
.pay{display:flex;justify-content:center;gap:5px;margin-top:18px}
.pay i{width:29px;height:18px;background:#fff;border-radius:2px;display:block}
.copy{position:absolute;left:0;right:0;bottom:0;height:46px;border-top:1px solid #3a3a3a;font-size:8.5px;display:flex;align-items:center;justify-content:center;gap:4px}
.copy b{color:var(--blue);font-weight:400}
</style>
</head>
<body>

<div class="topbar"><div class="wrap">
  <span>Net 30 Terms &nbsp;|&nbsp; Resellers &nbsp;|&nbsp; Track Your Shipment</span>
  <span>Free Shipping on orders $35 or more!</span>
  <span class="acct"><svg width="9" height="9" viewBox="0 0 10 10" fill="none" stroke="#0b5aaa"><circle cx="5" cy="3" r="2"/><path d="M1 9.5c0-2.5 8-2.5 8 0"/></svg><b>Hello</b> Login &nbsp;|&nbsp; Register</span>
</div></div>

<header class="header"><div class="wrap">
  <div class="brand"><i class="mark"></i><span>Brivonta</span></div>
  <div class="search">
    <div class="cat"><span>All Categories</span><span>⌄</span></div>
    <div class="q">Search by Title, Category ...</div>
    <div class="go"><svg width="13" height="13" viewBox="0 0 14 14" fill="none" stroke="#fff" stroke-width="1.6"><circle cx="6" cy="6" r="4.5"/><path d="M9.5 9.5l3 3"/></svg></div>
  </div>
  <div class="hinfo" style="margin-left:44px">
    <svg width="24" height="24" viewBox="0 0 24 24" fill="none" stroke="#0b5aaa" stroke-width="1.4"><path d="M6 3l3 4-2 2c1 3 4 6 7 7l2-2 4 3-2 3C11 20 4 13 3 5z"/></svg>
    <div>Live Chat Or:<strong>010-555-0182</strong></div>
  </div>
  <div class="hinfo" style="margin-left:36px">
    <span class="ico"><svg width="24" height="22" viewBox="0 0 24 22" fill="none" stroke="#0b5aaa" stroke-width="1.4"><path d="M12 20S2 13 2 7a5 5 0 0 1 10-1 5 5 0 0 1 10 1c0 6-10 13-10 13z"/></svg><i class="badge">0</i></span>
    <div>My Wishlist<strong>$00.00</strong></div>
  </div>
  <div class="hinfo" style="margin-left:22px">
    <span class="ico"><svg width="24" height="22" viewBox="0 0 24 22" fill="none" stroke="#0b5aaa" stroke-width="1.4"><path d="M1 3h4l3 12h12l2-9H7"/><circle cx="9" cy="19" r="1.5"/><circle cx="18" cy="19" r="1.5"/></svg><i class="badge">5</i></span>
    <div>My Shopping Cart<strong>$299.49</strong></div>
  </div>
</div></header>

<nav class="nav"><div class="wrap">
  <div class="allcat"><svg width="13" height="10" viewBox="0 0 13 10" stroke="#fff" stroke-width="1.3"><path d="M0 1h13M0 5h13M0 9h13"/></svg>All Categories <span style="margin-left:20px">⌄</span></div>
  <ul>
    <li>HOME</li><li>ABOUT US</li><li>PRODUCTS ⌄</li><li>SAFETY INFORMATION ⌄</li><li>DOWNLOADS</li><li>CONTACT US</li>
  </ul>
</div></nav>

<section class="hero">
  <svg class="arrow" style="left:50px" width="16" height="28" viewBox="0 0 16 28" fill="none" stroke="#333" stroke-width="1.5"><path d="M14 1L2 14l12 13"/></svg>
  <div class="text">
    <div class="kicker">Best offer for you</div>
    <h1><b>FIBREGLASS</b> LADDERS</h1>
    <p>South Africa’s Leading Manufacturer of Ladders, Trolleys, Castors, Wheels &amp; Ladder Accessories</p>
    <a class="btn">Shop Now &nbsp;›</a>
  </div>
  <div class="visual" role="img" aria-label="Blue steel platform trolley with two mesh end frames"></div>
  <svg class="arrow" style="left:1134px" width="16" height="28" viewBox="0 0 16 28" fill="none" stroke="#333" stroke-width="1.5"><path d="M2 1l12 13L2 27"/></svg>
  <div class="dots"><i></i><i class="on"></i><i></i></div>
</section>

<section class="features"><div class="wrap">
  <div class="feat"><svg width="48" height="38" viewBox="0 0 48 38" fill="none" stroke="#0b5aaa" stroke-width="1.5"><rect x="2" y="3" width="28" height="24"/><path d="M30 11h9l7 8v8H30"/><circle cx="11" cy="30" r="4"/><circle cx="38" cy="30" r="4"/></svg><h4>FREE DELIVERY</h4><p>Worldwide from $75</p></div>
  <div class="feat"><svg width="40" height="38" viewBox="0 0 40 38" fill="none" stroke="#0b5aaa" stroke-width="1.5"><path d="M14 8l14-6 10 6v14l-14 6-10-6z"/><path d="M14 8l10 6 14-6M24 14v14"/><path d="M3 26a8 8 0 1 0 8-8"/><path d="M3 20v6h6"/></svg><h4>EASY RETURNS</h4><p>30 days for free</p></div>
  <div class="feat"><svg width="46" height="38" viewBox="0 0 46 38" fill="none" stroke="#0b5aaa" stroke-width="1.5"><rect x="2" y="3" width="38" height="26" rx="2"/><path d="M2 10h38"/><rect x="7" y="16" width="8" height="6"/><circle cx="34" cy="28" r="8" fill="#fff"/><path d="M30 28l3 3 5-6"/></svg><h4>COMFORT PAYMENTS</h4><p>Credit Cards Available</p></div>
  <div class="feat"><svg width="38" height="38" viewBox="0 0 38 38" fill="none" stroke="#0b5aaa" stroke-width="1.5"><circle cx="19" cy="14" r="7"/><path d="M10 14a9 9 0 0 1 18 0M6 36c0-8 26-8 26 0"/><rect x="8" y="12" width="3" height="6"/><rect x="27" y="12" width="3" height="6"/></svg><h4>CUSTOMER SUPPORT</h4><p>Call or email us 24/7</p></div>
</div></section>

<section class="categories"><div class="wrap">
  <h2 class="sec-title">Our <span>Categories</span></h2>
  <p class="sec-lede">Lorem ipsum dolor sit amet, consectetur adipiscing elit, sed do eiusmod tempor incididunt ut labore et dolore magna aliqua.</p>
  <div class="cat-row">
    <span class="slide" style="left:-37px;top:70px"><svg width="8" height="10" viewBox="0 0 8 10" fill="none" stroke="#fff" stroke-width="1.4"><path d="M6 1L2 5l4 4"/></svg></span>
    <div class="cat"><div class="pic" role="img" aria-label="Platform trolley"></div><h5>CATEGORY NAME</h5><a class="btn">Shop Now &nbsp;›</a></div>
    <div class="cat"><div class="pic ladder" role="img" aria-label="Fibreglass step ladder"></div><h5>CATEGORY NAME</h5><a class="btn">Shop Now &nbsp;›</a></div>
    <div class="cat"><div class="pic" style="background:linear-gradient(180deg,#eee,#b9bcc2)" role="img" aria-label="Folding multi-purpose ladder"></div><h5>CATEGORY NAME</h5><a class="btn">Shop Now &nbsp;›</a></div>
    <div class="cat"><div class="pic" role="img" aria-label="Platform trolley"></div><h5>CATEGORY NAME</h5><a class="btn">Shop Now &nbsp;›</a></div>
    <div class="cat"><div class="pic ladder" role="img" aria-label="Fibreglass step ladder"></div><h5>CATEGORY NAME</h5><a class="btn">Shop Now &nbsp;›</a></div>
    <div class="cat"><div class="pic" role="img" aria-label="Platform trolley"></div><h5>CATEGORY NAME</h5><a class="btn">Shop Now &nbsp;›</a></div>
    <span class="slide" style="left:899px;top:70px"><svg width="8" height="10" viewBox="0 0 8 10" fill="none" stroke="#fff" stroke-width="1.4"><path d="M2 1l4 4-4 4"/></svg></span>
  </div>
</div></section>

<section class="products"><div class="wrap">
  <h2 class="sec-title">Find your <span>best products</span></h2>
  <p class="sec-lede">Lorem ipsum dolor sit amet, consectetur adipiscing elit, sed do eiusmod tempor incididunt ut labore et dolore magna aliqua.</p>
  <div class="tabs"><span>Top Rated Products</span><span class="on">Sale Products</span><span>Featured Products</span></div>
  <div class="grid">
    <span class="slide" style="left:-35px;top:140px"><svg width="8" height="10" viewBox="0 0 8 10" fill="none" stroke="#fff" stroke-width="1.4"><path d="M6 1L2 5l4 4"/></svg></span>
    <div class="card"><div class="pic"><div role="img" aria-label="Red hand truck"></div></div><span class="off">-30%<br>OFF</span><p class="cn">Category Name</p><h6>STEADY STEP KTV RANGE</h6><div class="stars">★★★★★</div><div class="foot"><span class="cartbtn"><svg width="13" height="12" viewBox="0 0 13 12" fill="none" stroke="#fff" stroke-width="1.3"><path d="M0 1h2l2 7h7l1-5H3"/><circle cx="5" cy="10.5" r=".8"/><circle cx="10" cy="10.5" r=".8"/></svg></span><div class="price"><s>$55.00</s><b>$35.00</b></div></div></div>
    <div class="card"><div class="pic"><div role="img" aria-label="Red hand truck"></div></div><span class="off">-30%<br>OFF</span><p class="cn">Category Name</p><h6>STEADY STEP KTV RANGE</h6><div class="stars">★★★★<em>★</em></div><div class="foot"><span class="cartbtn"><svg width="13" height="12" viewBox="0 0 13 12" fill="none" stroke="#fff" stroke-width="1.3"><path d="M0 1h2l2 7h7l1-5H3"/><circle cx="5" cy="10.5" r=".8"/><circle cx="10" cy="10.5" r=".8"/></svg></span><div class="price"><s>$55.00</s><b>$35.00</b></div></div></div>
    <div class="card"><div class="pic"><div role="img" aria-label="Red hand truck"></div></div><span class="off">-30%<br>OFF</span><p class="cn">Category Name</p><h6>STEADY STEP KTV RANGE</h6><div class="stars">★<em>☆☆☆☆</em></div><div class="foot"><span class="cartbtn"><svg width="13" height="12" viewBox="0 0 13 12" fill="none" stroke="#fff" stroke-width="1.3"><path d="M0 1h2l2 7h7l1-5H3"/><circle cx="5" cy="10.5" r=".8"/><circle cx="10" cy="10.5" r=".8"/></svg></span><div class="price"><s>$55.00</s><b>$35.00</b></div></div></div>
    <div class="card"><div class="pic"><div role="img" aria-label="Red hand truck"></div></div><span class="off">-30%<br>OFF</span><p class="cn">Category Name</p><h6>STEADY STEP KTV RANGE</h6><div class="stars">★★★<em>★☆</em></div><div class="foot"><span class="cartbtn"><svg width="13" height="12" viewBox="0 0 13 12" fill="none" stroke="#fff" stroke-width="1.3"><path d="M0 1h2l2 7h7l1-5H3"/><circle cx="5" cy="10.5" r=".8"/><circle cx="10" cy="10.5" r=".8"/></svg></span><div class="price"><s>$55.00</s><b>$35.00</b></div></div></div>
    <span class="slide" style="left:897px;top:140px"><svg width="8" height="10" viewBox="0 0 8 10" fill="none" stroke="#fff" stroke-width="1.4"><path d="M2 1l4 4-4 4"/></svg></span>
  </div>
</div></section>

<section class="why">
  <h2 class="sec-title">Why shop Brivonta</h2>
  <p class="sec-lede">Lorem ipsum dolor sit amet, consectetur adipiscing elit, sed do eiusmod tempor incididunt ut labore et dolore magna aliqua.</p>
  <div class="why-row">
    <div class="why-item"><div class="ring"><svg width="28" height="28" viewBox="0 0 28 28" fill="none" stroke="#fff" stroke-width="1.4"><path d="M4 4h4l5 16h8"/><rect x="11" y="7" width="10" height="9" transform="rotate(-15 16 11)"/><circle cx="14" cy="23" r="2"/></svg></div><h4>GET FREE SHIPPING</h4><p>Worldwide from $75</p></div>
    <div class="why-item"><div class="ring"><svg width="28" height="28" viewBox="0 0 28 28" fill="none" stroke="#fff" stroke-width="1.4"><circle cx="14" cy="14" r="11"/><path d="M7 10h2l2 7h8l1-5H10"/></svg></div><h4>EASY RETURNS</h4><p>30 days for free</p></div>
    <div class="why-item"><div class="ring"><svg width="28" height="28" viewBox="0 0 28 28" fill="none" stroke="#fff" stroke-width="1.4"><path d="M14 3l7 3v5c0 4-3 6-7 8-4-2-7-4-7-8V6z"/><path d="M11 11l2 2 4-4"/><path d="M3 22h6l4 2h8l4-3"/></svg></div><h4>COMFORT PAYMENTS</h4><p>Credit Cards Available</p></div>
  </div>
</section>

<section class="latest"><div class="wrap">
  <h2 class="sec-title">Our <span>latest products</span></h2>
  <p class="sec-lede">Lorem ipsum dolor sit amet, consectetur adipiscing elit, sed do eiusmod tempor incididunt ut labore et dolore magna aliqua.</p>
  <div class="grid">
    <span class="slide" style="left:-35px;top:140px"><svg width="8" height="10" viewBox="0 0 8 10" fill="none" stroke="#fff" stroke-width="1.4"><path d="M6 1L2 5l4 4"/></svg></span>
    <div class="card"><div class="pic"><div role="img" aria-label="Red hand truck"></div></div><span class="off">-30%<br>OFF</span><p class="cn">Category Name</p><h6>STEADY STEP KTV RANGE</h6><div class="stars">★★★★★</div><div class="foot"><span class="cartbtn"><svg width="13" height="12" viewBox="0 0 13 12" fill="none" stroke="#fff" stroke-width="1.3"><path d="M0 1h2l2 7h7l1-5H3"/><circle cx="5" cy="10.5" r=".8"/><circle cx="10" cy="10.5" r=".8"/></svg></span><div class="price"><s>$55.00</s><b>$35.00</b></div></div></div>
    <div class="card"><div class="pic"><div role="img" aria-label="Red hand truck"></div></div><span class="off">-30%<br>OFF</span><p class="cn">Category Name</p><h6>STEADY STEP KTV RANGE</h6><div class="stars">★★★★<em>★</em></div><div class="foot"><span class="cartbtn"><svg width="13" height="12" viewBox="0 0 13 12" fill="none" stroke="#fff" stroke-width="1.3"><path d="M0 1h2l2 7h7l1-5H3"/><circle cx="5" cy="10.5" r=".8"/><circle cx="10" cy="10.5" r=".8"/></svg></span><div class="price"><s>$55.00</s><b>$35.00</b></div></div></div>
    <div class="card"><div class="pic"><div role="img" aria-label="Red hand truck"></div></div><span class="off">-30%<br>OFF</span><p class="cn">Category Name</p><h6>STEADY STEP KTV RANGE</h6><div class="stars">★<em>☆☆☆☆</em></div><div class="foot"><span class="cartbtn"><svg width="13" height="12" viewBox="0 0 13 12" fill="none" stroke="#fff" stroke-width="1.3"><path d="M0 1h2l2 7h7l1-5H3"/><circle cx="5" cy="10.5" r=".8"/><circle cx="10" cy="10.5" r=".8"/></svg></span><div class="price"><s>$55.00</s><b>$35.00</b></div></div></div>
    <div class="card"><div class="pic"><div role="img" aria-label="Red hand truck"></div></div><span class="off">-30%<br>OFF</span><p class="cn">Category Name</p><h6>STEADY STEP KTV RANGE</h6><div class="stars">★★★<em>★☆</em></div><div class="foot"><span class="cartbtn"><svg width="13" height="12" viewBox="0 0 13 12" fill="none" stroke="#fff" stroke-width="1.3"><path d="M0 1h2l2 7h7l1-5H3"/><circle cx="5" cy="10.5" r=".8"/><circle cx="10" cy="10.5" r=".8"/></svg></span><div class="price"><s>$55.00</s><b>$35.00</b></div></div></div>
    <span class="slide" style="left:897px;top:140px"><svg width="8" height="10" viewBox="0 0 8 10" fill="none" stroke="#fff" stroke-width="1.4"><path d="M2 1l4 4-4 4"/></svg></span>
  </div>
</div></section>

<section class="brands"><div class="wrap">
  <h2 class="sec-title">Our <span>brands</span></h2>
  <div class="brand-row">
    <div>Korvello</div><div>Pinewick</div><div>Maroda</div><div>Tessaline</div><div>Orchard Lane</div><div>Korvello</div>
  </div>
</div></section>

<section class="subscribe">
  <svg width="26" height="24" viewBox="0 0 26 24" fill="none" stroke="#0b5aaa" stroke-width="1.5"><path d="M2 10l11-8 11 8v12H2z"/><path d="M2 10l11 7 11-7"/></svg>
  <h3>Subscribe</h3>
  <p>Get on the list and get 10% off your first order!</p>
  <div class="sub-form"><span>Enter Your E-Mail</span><b>SUBSCRIBE</b></div>
</section>

<footer class="footer">
  <div class="brand"><i class="mark"></i><span>Brivonta</span></div>
  <div class="flinks"><span>Home</span><span>About</span><span>Shop</span><span>News</span><span>Faq</span><span>Contact</span></div>
  <div class="pay"><i></i><i></i><i></i><i></i><i></i><i></i></div>
  <div class="copy">Copyright © 2022 Brivonta. All Rights Reserved | <b>010-555-0182</b> | contact@brivonta.example</div>
</footer>

</body>
</html>
```